RISE with Abbot Leng Book Cover

We need a Book cover for a Spiritual Book entitled:

R.I.S.E. with Abbot Leng: Reflective Inner Study Exercises with a Present Era Hermit Sage

By Ven. Abbot Leng Odile Rask, MPH

By 2x No. 1 Best Selling Author

See sketch: By 2x No. 1 Best Selling Author in WHITE Text
The tape where above is written and 1 in red Text

ABBOT LENG ODILE RASK, MPH (White and Thick BOLD TEXT - see attachment KE Baltor)

R.I.S.E. ABBOT LENG (Use the Wayfinder FONT and style in WHITE text/colour)

with (use the Corinne Haldwell book - No. 1 Best Seller Text Style in white or red)

Reflective Inner Study Exercises with a Present Era Hermit Sage (Use Harwick book - red block at the bottom)

Please clean up the picture as it is a raw file and take out the shadow on Abbot Leng's face. Make us more translucent and light filled. Clean up the face and crop to look like the sketch (cro just underneath the white cuff on Monk's sleeve). Keep to of pic as it to use the right hand space for By No. 1 Best Selling Author and No. 1 text and red band.

```html
<!DOCTYPE html>
<html lang="en">
<head>
<meta charset="utf-8">
<title>R.I.S.E. with Abbot Leng — Book Cover</title>
<link rel="stylesheet" href="https://fonts.googleapis.com/css2?family=Anton&family=Archivo+Black&family=Oswald:wght@500&family=Libre+Baskerville:ital,wght@1,700&display=swap">
<style>
  :root {
    --ink-deep: #0b2233;
    --ink-mid: #1d4a63;
    --white: #ffffff;
    --red: #e8121c;
    --shadow: rgba(0, 0, 0, 0.55);
  }
  * { margin: 0; padding: 0; box-sizing: border-box; }
  html, body {
    width: 751px; height: 1200px; overflow: hidden;
    background: var(--ink-deep);
  }
  .cover {
    position: relative; width: 751px; height: 1200px; overflow: hidden;
    background: var(--ink-deep);
  }
  .cover-photo {
    position: absolute; inset: 0;
    background:
      radial-gradient(ellipse 240px 300px at 190px 330px, rgba(220,235,240,0.5), transparent 70%),
      radial-gradient(ellipse 200px 260px at 540px 380px, rgba(220,235,240,0.45), transparent 70%),
      radial-gradient(ellipse 420px 300px at 620px 80px, rgba(90,150,175,0.45), transparent 75%),
      linear-gradient(180deg, var(--ink-mid) 0%, #163e55 45%, var(--ink-deep) 100%);
  }
  .author-line {
    position: absolute; top: 52px; left: 30px;
    font-family: "Archivo Black", "Arial Black", sans-serif;
    font-size: 25px; line-height: 1; letter-spacing: 0.3px; color: var(--white);
    text-shadow: 1px 2px 3px var(--shadow);
    white-space: nowrap;
  }
  .rank-mark {
    position: absolute; top: 42px; left: 652px;
    font-family: "Oswald", "Arial Narrow", sans-serif; font-weight: 500;
    font-size: 60px; line-height: 1; color: var(--red);
    text-shadow: 1px 1px 2px rgba(0,0,0,0.4);
  }
  .bestseller-ribbon { position: absolute; top: 0; right: 0; width: 260px; height: 260px; }
  .ribbon-label {
    font-family: "Libre Baskerville", Georgia, serif; font-style: italic; font-weight: 700;
    font-size: 17px; fill: var(--white); letter-spacing: 0.5px;
  }
  .title-block { color: var(--white); font-weight: normal; }
  .title-acronym, .title-with, .title-name {
    position: absolute; left: 0; right: 0; display: block;
    text-align: center; line-height: 1; white-space: nowrap;
  }
  .title-acronym, .title-name {
    font-family: "Anton", Impact, sans-serif;
    text-shadow: 3px 4px 5px var(--shadow);
  }
  .title-acronym { top: 590px; font-size: 134px; letter-spacing: 2px; }
  .title-with {
    top: 752px;
    font-family: "Oswald", "Arial Narrow", sans-serif; font-weight: 500;
    font-size: 46px;
    text-shadow: 2px 2px 4px var(--shadow);
  }
  .title-name {
    top: 818px; font-size: 168px;
    transform: scaleX(0.84); transform-origin: center;
  }
  .subtitle-box {
    position: absolute; left: 53px; top: 1010px; width: 663px; height: 161px;
    border: 2px solid var(--white); padding: 7px;
  }
  .subtitle-fill {
    width: 100%; height: 100%; background: var(--red);
    display: flex; align-items: center; justify-content: center;
    text-align: center; padding: 0 14px;
  }
  .subtitle {
    font-family: "Libre Baskerville", Georgia, serif; font-style: italic; font-weight: 700;
    font-size: 28px; line-height: 1.5; color: var(--white); text-transform: uppercase;
  }
</style>
</head>
<body>
<main class="cover">
  <div class="cover-photo" role="img" aria-label="Duotone photograph of an elderly monk and a smiling shaven-headed student facing each other in teal-blue tones"></div>

  <p class="author-line">ABBOT LENG&nbsp; ODILE RASK, MPH</p>

  <svg class="bestseller-ribbon" viewBox="0 0 260 260">
    <polygon points="16,0 82,0 260,178 260,244" fill="var(--red)"/>
    <polygon points="28,3 74,3 257,186 257,232" fill="none" stroke="var(--white)" stroke-width="1.2" opacity="0.85"/>
    <text class="ribbon-label" x="0" y="0" text-anchor="middle" transform="translate(150 108) rotate(45)">#1 BEST SELLING AUTHOR</text>
  </svg>

  <p class="rank-mark">#1</p>

  <h1 class="title-block">
    <span class="title-acronym">R.I.S.E.</span>
    <span class="title-with">with</span>
    <span class="title-name">ABBOT LENG</span>
  </h1>

  <div class="subtitle-box">
    <div class="subtitle-fill">
      <p class="subtitle">Reflective Inner Study Exercises<br>with a Present Era Hermit Sage</p>
    </div>
  </div>
</main>
</body>
</html>
```